Business Report Cover

We need a revamped quarterly report cover to send to our clients. We asset manage commercial and residential properties throughout the the United States. We use a .pdf version of a cover that we've used for years but would like a fresh updated look for 2018. The cover should include our company logo (KVL Holdings) and a photo of the property as well as the Quarter/Year of the report.

Industry/Entity Type

Business

```html
<!DOCTYPE html>
<html lang="en">
<head>
<meta charset="UTF-8">
<title>KVL Holdings — Quarterly Operating Report, 1st Quarter 2017</title>
<link rel="stylesheet" href="https://fonts.googleapis.com/css2?family=Montserrat:wght@300;400;700&display=swap">
<style>
  :root {
    --backdrop: #e6e6e6;
    --green: #1f7a45;
    --green-light: #2f9a5a;
    --green-veil: rgba(27, 118, 64, 0.82);
    --ink: #1d1d1d;
    --white: #ffffff;
    --sky-top: #dfe6ea;
    --sky-low: #c9d3d6;
    --pavement: #7d8185;
    --foliage: #4f6b3e;
  }
  * { box-sizing: border-box; margin: 0; padding: 0; }
  html, body {
    width: 1200px;
    height: 790px;
    overflow: hidden;
    background: var(--backdrop);
    font-family: "Montserrat", sans-serif;
  }
  .report-cover {
    position: absolute;
    left: 314px;
    top: 25px;
    width: 572px;
    height: 740px;
    overflow: hidden;
    background: var(--white);
    box-shadow: 0 6px 18px rgba(0, 0, 0, 0.18);
  }
  .property-photo {
    position: absolute;
    inset: 0;
    background: linear-gradient(180deg,
      var(--sky-top) 0%,
      var(--sky-low) 38%,
      #a9a39a 46%,
      #8a4a3c 52%,
      var(--foliage) 62%,
      var(--pavement) 70%,
      #8c9094 100%);
  }
  .brand-band {
    position: absolute;
    top: 0;
    left: 330px;
    width: 170px;
    height: 100%;
    background: var(--green-veil);
  }
  .brand-band__cap {
    position: absolute;
    top: 0;
    left: 0;
    right: 0;
    height: 34px;
    background: var(--green-light);
  }
  .brand-band__solid {
    position: absolute;
    top: 34px;
    left: 0;
    right: 0;
    height: 260px;
    background: var(--green);
  }
  .logo-panel {
    position: absolute;
    top: 34px;
    left: 330px;
    width: 205px;
    height: 92px;
    background: var(--white);
    display: flex;
    align-items: center;
    justify-content: center;
    gap: 8px;
  }
  .logo-panel__mark {
    width: 10px;
    height: 10px;
    background: var(--green);
  }
  .logo-panel__name {
    font-weight: 700;
    font-size: 22px;
    letter-spacing: 1px;
    color: var(--ink);
  }
  .report-title {
    position: absolute;
    left: 330px;
    width: 170px;
    top: 470px;
    padding-left: 22px;
    color: var(--white);
  }
  .report-title__label {
    font-weight: 300;
    font-size: 9px;
    letter-spacing: 0.3px;
    margin-bottom: 6px;
  }
  .report-title__quarter {
    font-weight: 300;
    font-size: 20px;
    padding-bottom: 4px;
    border-bottom: 1px solid var(--white);
    width: 128px;
  }
  .report-title__year {
    font-weight: 700;
    font-size: 40px;
    letter-spacing: 1px;
    margin-top: 2px;
  }
  .property-address {
    position: absolute;
    left: 78px;
    bottom: 96px;
    font-weight: 300;
    font-size: 12px;
    line-height: 1.35;
    color: var(--white);
  }
</style>
</head>
<body>
  <main class="report-cover">
    <div class="property-photo" role="img" aria-label="Photograph of the property: a convenience store with a fuel canopy and pumps, landscaped shrubs and a paved lot under a cloudy sky"></div>

    <div class="brand-band">
      <div class="brand-band__cap"></div>
      <div class="brand-band__solid"></div>
    </div>

    <div class="logo-panel">
      <span class="logo-panel__mark"></span>
      <span class="logo-panel__name">KVL Holdings</span>
    </div>

    <section class="report-title">
      <p class="report-title__label">Quarterly Operating Report</p>
      <p class="report-title__quarter">1st Quarter</p>
      <p class="report-title__year">2017</p>
    </section>

    <address class="property-address">
      Harbor Point Market<br>
      4120 NE Lakeside Commons Dr.<br>
      Fairhaven, WA 98225
    </address>
  </main>
</body>
</html>
```